Website/Logo Design

We need a logo and website design for an opinion mining startup called VantaLume. Our technology mines the web to automatically discover what people are saying about brands, products, etc. The project we are fielding here is for our informational, public-facing website. In its initial incarnation, it will simply be a vehicle for marketing materials and information on our company and its offerings, but it should be flexible enough to expand as more content/functionality is added.

Some designs we like are:
http://www.tradewhisk.example
http://www.gorvantel.example
http://www.kfz.example
http://www.lintwharf.example
http://moxbarrel.example
http://trundlemq.example
http://www.zopla.example
Updates

All, please try to shy away from using a photo of a person as the focal point of the design.  Our company is more technological than social.

Target Market(s)

Primarily businesses interested in sentiment analysis (typically companies involved in advertising, market research, PR, etc.)

Industry/Entity Type

It Company

Requirements
Must have
• We are looking for a clean, modern, and professional design. This includes a logo, homepage, and internal page if it will differ from the homepage.
Nice to have
• It would be excellent if you could provide an HTML mockup if your design is chosen.
Should not have
• Flash, excessive bells and whistles

```html
<!DOCTYPE html>
<html lang="en">
<head>
<meta charset="utf-8">
<title>VantaLume – Opinion Mining</title>
<link rel="stylesheet" href="https://fonts.googleapis.com/css2?family=Open+Sans:wght@400;600&display=swap">
<style>
:root{
  --page:#e9e9ea;
  --page-top:#f6f6f8;
  --ink:#4a4a4a;
  --muted:#8a8a8a;
  --hero-text:#8d8f99;
  --pink:#d68fc4;
  --purple:#6a4596;
  --purple-dark:#3f2a68;
  --band-a:#5b3d8a;
  --band-b:#4a2f77;
  --lavender:#a58ac8;
  --pill:#a9a9ab;
  --white:#ffffff;
  --clients-a:#a7a7a7;
  --clients-b:#8f8f8f;
  --logo-ink:#5d4a86;
  --font:"Open Sans", sans-serif;
}
*{box-sizing:border-box;margin:0;padding:0}
html,body{width:1200px;height:1104px;overflow:hidden}
body{
  font-family:var(--font);
  color:var(--ink);
  background:radial-gradient(ellipse 700px 260px at 330px 110px,var(--page-top),var(--page) 70%),var(--page);
  position:relative;
}
.brand{position:absolute;left:82px;top:96px;font-size:50px;line-height:68px;font-weight:600;letter-spacing:-1px;color:var(--logo-ink)}
.nav{position:absolute;top:117px;left:0;width:1200px;height:27px;list-style:none}
.nav li{position:absolute;top:0;height:27px;border-radius:14px;background:var(--pill);color:var(--white);
  font-size:15px;line-height:27px;text-align:center;box-shadow:0 3px 6px rgba(0,0,0,.12)}
.nav li.active{background:var(--purple-dark)}
.hero{position:absolute;left:38px;top:187px;width:1110px;height:252px;border-radius:10px 10px 0 0;overflow:hidden;
  background:linear-gradient(100deg,#e4e7f2 0%,#f7f8fc 30%,#ffffff 70%)}
.hero-questions{position:absolute;right:400px;top:47px;text-align:right;color:var(--hero-text);font-size:18px;line-height:37px;white-space:nowrap}
.hero-questions em{font-style:normal;color:var(--pink)}
.answer{position:absolute;left:431px;top:176px;width:301px;height:47px;border-radius:5px;
  background:linear-gradient(var(--lavender),#8f6fbb);color:var(--white);font-size:19px;line-height:47px;text-align:center}
.answer svg{position:absolute;left:238px;top:46px}
.hero-visual{position:absolute;left:763px;top:0;width:347px;height:252px;
  background:linear-gradient(180deg,rgba(236,232,244,0) 0%,#ece7f3 100%)}
.features{position:absolute;left:38px;top:439px;width:1110px;height:119px;border-radius:0 0 8px 8px;
  background:linear-gradient(var(--band-a),var(--band-b));display:flex;box-shadow:0 14px 20px -10px rgba(0,0,0,.2)}
.feature{position:relative;height:100%;color:var(--white);font-size:15px;line-height:20px}
.feature + .feature{border-left:1px solid rgba(0,0,0,.25);box-shadow:inset 1px 0 0 rgba(255,255,255,.08)}
.feature svg{position:absolute;top:32px}
.feature p{position:absolute;top:26px;white-space:nowrap}
.col{position:absolute;top:598px}
.col h2{font-weight:400;font-size:23px;color:#333;margin-bottom:20px}
.col p{font-size:16px;line-height:23px;color:var(--muted)}
.about{left:83px;width:320px}
.more{position:absolute;left:169px;top:168px;width:148px;height:27px;border-radius:14px;background:#cfcfd0;
  color:var(--white);font-size:15px;line-height:27px;text-align:center}
.services{left:444px;width:330px}
.services ul{list-style:none}
.services li{position:relative;padding-left:30px;color:var(--purple);font-size:16px;line-height:19px;margin-bottom:19px}
.services li svg{position:absolute;left:0;top:1px}
.contact{left:810px;width:340px}
.contact .name{color:#555;font-size:16px;margin-bottom:16px}
.contact dl{display:grid;grid-template-columns:92px auto;font-size:16px;line-height:23px;color:var(--muted);margin-top:20px}
.contact dd{color:var(--muted)}
.contact a{color:var(--purple);text-decoration:none}
.clients{position:absolute;left:38px;top:910px;width:1110px;height:100px;border-radius:10px;
  background:linear-gradient(90deg,var(--clients-a),var(--clients-b));box-shadow:0 10px 18px -8px rgba(0,0,0,.25)}
.clients h3{position:absolute;left:48px;top:38px;font-weight:400;font-size:18px;color:var(--white)}
.client{position:absolute;top:38px;width:130px;margin-left:-65px;text-align:center;font-size:19px;font-weight:600;color:#c9c9c9}
.client.active{color:var(--white)}
.footer{position:absolute;left:82px;top:1036px;font-size:13px;color:#777}
.footer a{color:var(--purple);text-decoration:none}
.footer nav{position:absolute;left:237px;top:0;white-space:nowrap}
</style>
</head>
<body>
<header>
  <div class="brand">VantaLume</div>
  <ul class="nav">
    <li style="left:507px;width:147px">About VantaLume</li>
    <li style="left:676px;width:128px">How We Work</li>
    <li class="active" style="left:825px;width:121px">Case Studies</li>
    <li style="left:967px;width:78px">Pricing</li>
    <li style="left:1066px;width:82px">Contact</li>
  </ul>
</header>

<section class="hero">
  <div class="hero-questions">
    <p>What do <em>users think</em> about your product?</p>
    <p>Are your <em>clients satisfied</em> with your services?</p>
    <p>Does your company create a <em>positive vibe</em> on the Internet?</p>
  </div>
  <div class="answer">VantaLume knows the answer.
    <svg width="22" height="16" viewBox="0 0 22 16"><path d="M0 0H22L20 16Z" fill="#8f6fbb"/></svg>
  </div>
  <div class="hero-visual" role="img" aria-label="Hero image area beside the questions"></div>
</section>

<section class="features">
  <div class="feature" style="width:378px">
    <svg style="left:46px" width="56" height="56" viewBox="0 0 56 56">
      <rect x="4" y="6" width="44" height="46" rx="3" fill="#f2f2f2"/>
      <rect x="10" y="30" width="7" height="18" fill="#e0453a"/>
      <rect x="19" y="20" width="7" height="28" fill="#f2a231"/>
      <rect x="28" y="24" width="7" height="24" fill="#3f8fd6"/>
      <rect x="37" y="14" width="7" height="34" fill="#63b845"/>
    </svg>
    <p style="left:118px">Get comprehensive charts,<br>graphs and reports. Results with<br>quick overview.</p>
  </div>
  <div class="feature" style="width:377px">
    <svg style="left:28px" width="56" height="50" viewBox="0 0 56 50">
      <ellipse cx="22" cy="18" rx="20" ry="14" fill="#8cc63f"/>
      <path d="M12 28L8 38L20 31Z" fill="#8cc63f"/>
      <ellipse cx="36" cy="30" rx="16" ry="11" fill="#e58fc6"/>
      <path d="M44 38L50 46L40 40Z" fill="#e58fc6"/>
    </svg>
    <p style="left:113px">It´s also about the details -<br>you get quotations and exact<br>thoughts from your customers.</p>
  </div>
  <div class="feature" style="width:355px">
    <svg style="left:20px;top:38px" width="54" height="44" viewBox="0 0 54 44">
      <path d="M2 14H28V2L52 22L28 42V30H2Z" fill="#8cc63f"/>
    </svg>
    <p style="left:90px">Take your marketing surveys<br>further - we have the skills, the<br>technique and equipment.</p>
  </div>
</section>

<section class="col about">
  <h2>About VantaLume</h2>
  <p>Duis eu ipsum sed orci tincidunt rutrum. Pellentesque a justo eget odio bibendum venenatis sed at tellus. Nulla non neque sit amet leo placerat.</p>
  <div class="more">About VantaLume</div>
</section>

<section class="col services">
  <h2>Our Services</h2>
  <ul>
    <li><svg width="16" height="14" viewBox="0 0 16 14"><path d="M1 7L6 12L15 1" fill="none" stroke="#d68fc4" stroke-width="2.5"/></svg>Acerat incidunt rutrum pellentesque justo parturient montes</li>
    <li><svg width="16" height="14" viewBox="0 0 16 14"><path d="M1 7L6 12L15 1" fill="none" stroke="#d68fc4" stroke-width="2.5"/></svg>Eget odio bibendum venenatis</li>
    <li><svg width="16" height="14" viewBox="0 0 16 14"><path d="M1 7L6 12L15 1" fill="none" stroke="#d68fc4" stroke-width="2.5"/></svg>Suspendisse interdum arcu in nisl condimentum</li>
    <li><svg width="16" height="14" viewBox="0 0 16 14"><path d="M1 7L6 12L15 1" fill="none" stroke="#d68fc4" stroke-width="2.5"/></svg>Nulla non neque sit phasellus sed mauris a sem mattis</li>
  </ul>
</section>

<section class="col contact">
  <h2>Contact Us</h2>
  <p class="name">VantaLume Ltd.</p>
  <p>42 Harrowgate Lane<br>KLM QT 4410, Brindlemoor, United Kingdom</p>
  <dl>
    <dt>Tel:</dt><dd>0044-371-62047</dd>
    <dt>E-mail:</dt><dd><a href="mailto:info@vantalume.example">info@vantalume.example</a></dd>
  </dl>
</section>

<section class="clients">
  <h3>Some of our clients...</h3>
  <span class="client" style="left:337px">Norvex</span>
  <span class="client" style="left:476px">Quellar</span>
  <span class="client" style="left:614px">Brantiva</span>
  <span class="client" style="left:753px">Taluno</span>
  <span class="client active" style="left:891px">Ferrox</span>
  <span class="client" style="left:1031px">Sonelo</span>
</section>

<footer class="footer">
  Copyright 2010, VantaLume Ltd.
  <nav><a href="#">Terms of Use</a> &nbsp;/&nbsp; <a href="#">Contact</a></nav>
</footer>
</body>
</html>
```